FAST TURNAROUND - simple sound/yoga event postcard

If you are up for a fast turnaround project within the next few hours then please submit your ideas. I have a photo, the text and a drawing of my idea for the front of the postcard.
PLEASE! Don't submit designs unless you are available now and can go back and forth to complete this project quickly -thank you-
PLEASE READ DETAILS FIRST - some designers are asking questions about things that I have outlined and specified in the brief -PLEASE LOOK AT ALL THE FILES - I have a doc about my ideas for the FRONT that are specific- thanks

FRONT OF THE POST CARD:
Please do not put anything else on the front other than the text on my instruction doc
I would like the lettering on the front of the card to be white or black (or white with black border) with simple fonts. However, I'm open to seeing the words WILLOW DRIFT in color blue for contrast
OPTION #1 for placing the title Willow Drift is to have the letter inside the gong (see my ideas for the front uploaded doc)
OPTION #2 for placing the title WILLOW DRIFT is the upper left part of the postcard.
lettering for lower left is Sound + Yogic Sleep (yoga nidra)

BACK OF THE POSTCARD:
BLACK BACKGROUND with white lettering. would love to see a couple of ideas of how you think the layout might look. I am open to only my website address being in blue as a contrast (or any of the other text) I've uploaded my logo but only on back side please keep it small
THANK YOU!

Target Market(s)

Yoga Students

Industry/Entity Type

Event

Requirements
Must have
• Must be 4.25 X 6.25 with bleed line CMYK - 300dpi PDF that follows the printers template (see uploaded files)
PLEASE READ INSTRUCTIONS ABOVE

Simple design please
Nice to have
• SEE ABOVE
Should not have
• LOGO NOT ON FRONT OF CARD
NO COLOR ON FRONT OF CARD JUST B AND W - maybe Willow Drift in color blue only

```html
<!DOCTYPE html>
<html lang="en">
<head>
<meta charset="utf-8">
<title>Willow Drift – Postcard</title>
<link rel="stylesheet" href="https://fonts.googleapis.com/css2?family=Comfortaa:wght@400;600&family=Didact+Gothic&family=Open+Sans:wght@700&display=swap">
<style>
  :root {
    --stage: #3b2a20;
    --ink-white: #ffffff;
    --card-black: #000000;
    --gong-dark: #26262a;
    --gong-mid: #5b5a5c;
    --temple-light: #d8d3cb;
    --temple-mid: #9d9892;
    --accent-orange: #f39a1e;
  }
  * { margin: 0; padding: 0; box-sizing: border-box; }
  html, body { width: 1200px; height: 1000px; overflow: hidden; }
  body { background: var(--stage); position: relative; }

  .postcard {
    position: absolute;
    width: 627px;
    height: 418px;
    overflow: hidden;
    box-shadow: 0 4px 14px rgba(0,0,0,0.45);
  }
  .postcard--front-corner { left: 25px; top: 70px; }
  .postcard--front-arc { left: 563px; top: 129px; }
  .postcard--back { left: 236px; top: 568px; height: 419px; background: var(--card-black); }

  .gong-photo {
    position: absolute;
    inset: 0;
    background:
      radial-gradient(circle at var(--gx) var(--gy), var(--gong-dark) 0 150px, var(--gong-mid) 180px, #3a393b 205px, var(--temple-mid) 215px, var(--temple-light) 330px);
  }
  .postcard--front-corner .gong-photo { --gx: 305px; --gy: 200px; }
  .postcard--front-arc .gong-photo { --gx: 317px; --gy: 202px; }

  .card-title {
    position: absolute;
    left: 32px;
    top: 30px;
    font-family: "Comfortaa", sans-serif;
    font-weight: 600;
    font-size: 29px;
    letter-spacing: 2px;
    color: var(--ink-white);
    text-shadow: 0 0 2px #000, 0 0 1px #000;
  }
  .card-tagline {
    position: absolute;
    left: 32px;
    bottom: 22px;
    font-family: "Open Sans", sans-serif;
    font-weight: 700;
    font-size: 12px;
    color: var(--ink-white);
    text-shadow: 0 0 2px #000;
  }
  .arc-title {
    position: absolute;
    inset: 0;
  }
  .arc-title text {
    font-family: "Comfortaa", sans-serif;
    font-weight: 600;
    font-size: 33px;
    letter-spacing: 5px;
    fill: var(--ink-white);
  }

  .brand-mark {
    position: absolute;
    left: 0; right: 0;
    top: 135px;
    display: flex;
    justify-content: center;
    align-items: center;
    gap: 8px;
  }
  .brand-dot {
    width: 22px; height: 22px;
    border-radius: 50%;
    background: var(--accent-orange);
  }
  .brand-name {
    font-family: "Didact Gothic", sans-serif;
    font-size: 16px;
    letter-spacing: 2px;
    color: var(--ink-white);
  }
  .website {
    position: absolute;
    left: 0; right: 0;
    top: 198px;
    text-align: center;
    font-family: "Didact Gothic", sans-serif;
    font-size: 15px;
    letter-spacing: 4.6px;
    color: var(--ink-white);
  }
</style>
</head>
<body>

  <section class="postcard postcard--front-corner">
    <div class="gong-photo" role="img" aria-label="Black and white photo of a large temple gong with eight small bosses around a central dome, ornate temple behind"></div>
    <h1 class="card-title">WILLOW DRIFT</h1>
    <p class="card-tagline">Sound + Yogic Sleep (yoga nidra)</p>
  </section>

  <section class="postcard postcard--front-arc">
    <div class="gong-photo" role="img" aria-label="Black and white photo of a large temple gong with eight small bosses around a central dome, ornate temple behind"></div>
    <svg class="arc-title" width="627" height="418" viewBox="0 0 627 418">
      <defs>
        <path id="gong-arc" d="M 165 210 A 152 152 0 0 1 469 210"/>
      </defs>
      <text><textPath href="#gong-arc" startOffset="50%" text-anchor="middle">WILLOW DRIFT</textPath></text>
    </svg>
    <p class="card-tagline">Sound + Yogic Sleep (yoga nidra)</p>
  </section>

  <section class="postcard postcard--back">
    <div class="brand-mark">
      <span class="brand-dot"></span>
      <span class="brand-name">Willow Drift</span>
    </div>
    <p class="website">www.willowdriftsound.com</p>
  </section>

</body>
</html>
```